Professional New Resume for personal/ company

Specialist in construction law, disputes and quantity surveying. Looking for a new fresh CV to appeal to the middle east (UAE) market.

Target Market(s)

employers, clients, lawyers, expert witnesses

Industry/Entity Type

Construction law, quantity surveying, dispute resolution.

```html
<!DOCTYPE html>
<html lang="en">
<head>
<meta charset="utf-8">
<title>Callum J Rennie – Curriculum Vitae</title>
<link rel="stylesheet" href="https://fonts.googleapis.com/css2?family=Tinos:wght@400;700&family=Roboto+Slab:wght@700&display=swap">
<style>
  :root{
    --backdrop:#30333d;
    --paper:#ffffff;
    --brand-blue:#0b5bb5;
    --ink:#2b2b2b;
    --ink-soft:#3d3d3d;
    --frame:#6d6d6d;
  }
  *{box-sizing:border-box;margin:0;padding:0}
  html,body{width:1200px;height:1095px;overflow:hidden;background:var(--backdrop)}
  .stage{position:absolute;left:0;top:0;width:2016px;height:1840px;zoom:0.595238}
  .page{position:absolute;width:514px;height:727px;background:var(--paper);overflow:hidden;font-family:"Tinos",serif;color:var(--ink-soft)}
  .page--one{left:426px;top:263px}
  .page--two{left:981px;top:263px}
  .page--three{left:426px;top:1046px}
  .page--four{left:981px;top:1046px}

  .band-top{position:absolute;left:413px;top:0;width:101px;height:172px;background:var(--brand-blue)}
  .band-foot{position:absolute;left:413px;top:687px;width:101px;height:40px;background:var(--brand-blue)}
  .brand{position:absolute;left:171px;top:26px;width:166px;text-align:center;font-family:"Tinos",serif;font-size:20px;font-weight:400;letter-spacing:1px;color:var(--brand-blue)}
  .name-frame{position:absolute;left:31px;top:87px;width:443px;height:72px;background:var(--paper);border:1.4px solid var(--frame);box-shadow:4px 3px 0 -1px var(--paper),4px 3px 0 0 var(--frame)}
  .portrait{position:absolute;left:42px;top:43px;width:108px;height:108px;border-radius:50%;background:radial-gradient(circle at 50% 70%,#4a4a4a 0%,#2f2f2f 30%,var(--brand-blue) 58%,var(--brand-blue) 100%)}
  .name{position:absolute;left:177px;top:102px;font-family:"Roboto Slab",serif;font-weight:700;font-size:27px;letter-spacing:2.2px;color:var(--brand-blue);white-space:nowrap}
  .creds{position:absolute;left:177px;top:133px;font-size:6.4px;font-weight:700;color:var(--ink);white-space:nowrap}
  .contact{position:absolute;font-size:6.5px;font-weight:700;color:var(--brand-blue);white-space:nowrap;display:flex;align-items:center;gap:4px}
  .contact svg{width:6px;height:6px;fill:var(--ink)}
  .contact--address{left:85px;top:170px}
  .contact--phone{left:85px;top:184px}
  .contact--email{left:275px;top:184px}

  .rail{position:absolute;width:3px;background:var(--brand-blue)}
  .section-title{position:absolute;font-size:11px;font-weight:700;color:var(--ink);white-space:nowrap}
  .section-title::before{content:"";position:absolute;left:-20px;top:2px;width:8px;height:8px;border:2px solid var(--brand-blue);border-radius:50%;background:var(--paper)}
  .prose{position:absolute;left:57px;width:409px;font-size:7.6px;line-height:14.7px;letter-spacing:.55px;text-align:justify}
  .list{position:absolute;left:57px;list-style:none;font-size:7.6px;line-height:14.7px;letter-spacing:.55px;white-space:nowrap}

  .entries{position:absolute;font-size:7px;line-height:13px;letter-spacing:.45px;white-space:nowrap}
  .entry{display:grid;grid-template-columns:62px 1fr;margin-bottom:13px}
  .entry--tight{margin-bottom:0}
  .entry dt{grid-column:1}
  .entry dd{grid-column:2}
  .timeline-row{display:grid;grid-template-columns:93px 1fr}
  .timeline-row--gap{margin-top:13px}
  .history-row{display:grid;grid-template-columns:155px 1fr}
  .outdent{margin-left:-31px}
</style>
</head>
<body>
<main class="stage">

  <article class="page page--one">
    <div class="band-top"></div>
    <div class="brand">Halden Resolve</div>
    <div class="name-frame"></div>
    <div class="portrait" role="img" aria-label="Portrait photograph of Callum J Rennie on a blue circle"></div>
    <h1 class="name">Callum J Rennie</h1>
    <p class="creds">BSc (Hons), Dip.Adj, LL.M, FCAP, FGPCS, MSCWS, MSCM</p>
    <p class="contact contact--address"><svg viewBox="0 0 10 10"><path d="M5 0a3.5 3.5 0 0 0-3.5 3.5C1.5 6 5 10 5 10s3.5-4 3.5-6.5A3.5 3.5 0 0 0 5 0zm0 5a1.5 1.5 0 1 1 0-3 1.5 1.5 0 0 1 0 3z"/></svg>3rd Floor, 18 Corran Terrace, Glasgow, Scotland, United Kingdom, G3 7QL</p>
    <p class="contact contact--phone"><svg viewBox="0 0 10 10"><path d="M1 3c0-1 1-2 4-2s4 1 4 2l-2 1-.5-1h-3L3 4 1 3zm1.5 1.5h5L9 9H1z"/></svg>+44 (0)7700 900 418</p>
    <p class="contact contact--email"><svg viewBox="0 0 10 10"><path d="M0 2h10v6H0zm1 1 4 3 4-3z"/></svg>callum@haldenresolve.co.uk</p>

    <div class="rail" style="left:31px;top:220px;height:390px"></div>
    <h2 class="section-title" style="left:48px;top:247px">Overview</h2>
    <p class="prose" style="top:269px">Adjudicator, Chartered Quantity Surveyor and Chartered Construction Manager with experience in Private Practice, Development and Main Contracting industry. Claims, contract and dispute resolution (adjudication) services (as adjudicator or party representative) provided in Scotland, England and Wales.</p>
    <p class="prose" style="top:342px">Qualifications include:- a BSc (Hons) in Quantity Surveying, LL.M Masters of Law (Construction Law), Fellow of The College of Arbitral Practitioners (FCAP), Fellow of The Guild of Property and Cost Surveyors (FGPCS); Member of The Society of Civil Works Surveyors (MSCWS) and a Professional Member of The Society of Construction Managers (MSCM). Experience includes involvement in a large and complex international arbitration. Experienced in BFC, SBF, ECF3/4 and IWC.</p>
    <h2 class="section-title" style="left:48px;top:458px">Qualifications/ Memberships</h2>
    <ul class="list" style="top:480px">
      <li>BSc (Hons) Quantity Surveying (Clydeside Technical University) (part-time)</li>
      <li>LL.M Masters of Law (Construction Law) (Kelvin University) (with Merit)</li>
      <li>Diploma in Adjudication (CAP)</li>
      <li>Fellow of The College of Arbitral Practitioners</li>
      <li>Fellow of The Guild of Property and Cost Surveyors</li>
      <li>Member of The Society of Civil Works Surveyors</li>
      <li>Member of The Society of Construction Managers</li>
      <li>Adjudicator &amp; Panel Member – NAP (Northern Adjudicators Panel)</li>
    </ul>
    <div class="band-foot"></div>
  </article>

  <article class="page page--two">
    <div class="band-top"></div>
    <div class="brand">Halden Resolve</div>
    <div class="name-frame"></div>
    <div class="portrait" role="img" aria-label="Portrait photograph of Callum J Rennie on a blue circle"></div>
    <h1 class="name">Callum J Rennie</h1>
    <p class="creds">BSc (Hons), Dip.Adj, LL.M, FCAP, FGPCS, MSCWS, MSCM</p>
    <p class="contact contact--address"><svg viewBox="0 0 10 10"><path d="M5 0a3.5 3.5 0 0 0-3.5 3.5C1.5 6 5 10 5 10s3.5-4 3.5-6.5A3.5 3.5 0 0 0 5 0zm0 5a1.5 1.5 0 1 1 0-3 1.5 1.5 0 0 1 0 3z"/></svg>3rd Floor, 18 Corran Terrace, Glasgow, Scotland, United Kingdom, G3 7QL</p>
    <p class="contact contact--phone"><svg viewBox="0 0 10 10"><path d="M1 3c0-1 1-2 4-2s4 1 4 2l-2 1-.5-1h-3L3 4 1 3zm1.5 1.5h5L9 9H1z"/></svg>+44 (0)7700 900 418</p>
    <p class="contact contact--email"><svg viewBox="0 0 10 10"><path d="M0 2h10v6H0zm1 1 4 3 4-3z"/></svg>callum@haldenresolve.co.uk</p>

    <div class="rail" style="left:35px;top:220px;height:460px"></div>
    <h2 class="section-title" style="left:53px;top:247px">Experience</h2>
    <div class="entries" style="left:59px;top:266px">
      <dl class="entry"><dt>Project:</dt><dd>Confidential</dd><dt>Value:</dt><dd>£1.2bn claim &amp; counter-claim</dd><dt>For:</dt><dd>Parties to an International Arbitration</dd><dt>Date:</dt><dd>December 2020 to Current</dd><dt>Services:</dt><dd>Tribunal secretary to assist the Arbitral Tribunal (Chairman<br>(Martin Hale KC) and two co-arbitrators (Sir Edmund Crane and Neil Ashby OBE, KC).</dd></dl>
      <dl class="entry"><dt>Project:</dt><dd>Various</dd><dt>Value:</dt><dd>Various</dd><dt>For:</dt><dd>Adjudicator in Construction Disputes, nominated by Northern Adjudicators Panel.</dd><dt>Date:</dt><dd>October 2021 to current.</dd><dt>Services:</dt><dd>Adjudicator</dd></dl>
      <dl class="entry"><dt>Project:</dt><dd>Flat Development, Edinburgh</dd><dt>Value:</dt><dd>£24,000</dd><dt>For:</dt><dd>Referring Party (Contractor)</dd><dt>Date:</dt><dd>December 2020</dd><dt>Services:</dt><dd>Representative for Referring Party</dd></dl>
      <dl class="entry"><dt>Project:</dt><dd>Supermarkets (various)</dd><dt>Value:</dt><dd>Various</dd><dt>For:</dt><dd>Referring Party (Subcontractor)</dd><dt>Date:</dt><dd>January 2019</dd><dt>Services:</dt><dd>Representative for Referring Party</dd></dl>
      <dl class="entry"><dt>Project:</dt><dd>Confidential</dd><dt>Value:</dt><dd>£2bn</dd><dt>For:</dt><dd>Brennock plc (consulting for Veltrix International)</dd><dt>Date:</dt><dd>February 2019 to Current</dd><dt>Services:</dt><dd>Conclude and implement compensation event quotations under ECF3/4 contracts.<br>Commercial management services, procurement advice, dispute avoidance.</dd></dl>
    </div>
    <div class="band-foot"></div>
  </article>

  <article class="page page--three">
    <div class="band-top"></div>
    <div class="brand">Halden Resolve</div>
    <div class="name-frame"></div>
    <div class="portrait" role="img" aria-label="Portrait photograph of Callum J Rennie on a blue circle"></div>
    <h1 class="name">Callum J Rennie</h1>
    <p class="creds">BSc (Hons), Dip.Adj, LL.M, FCAP, FGPCS, MSCWS, MSCM</p>
    <p class="contact contact--address"><svg viewBox="0 0 10 10"><path d="M5 0a3.5 3.5 0 0 0-3.5 3.5C1.5 6 5 10 5 10s3.5-4 3.5-6.5A3.5 3.5 0 0 0 5 0zm0 5a1.5 1.5 0 1 1 0-3 1.5 1.5 0 0 1 0 3z"/></svg>3rd Floor, 18 Corran Terrace, Glasgow, Scotland, United Kingdom, G3 7QL</p>
    <p class="contact contact--phone"><svg viewBox="0 0 10 10"><path d="M1 3c0-1 1-2 4-2s4 1 4 2l-2 1-.5-1h-3L3 4 1 3zm1.5 1.5h5L9 9H1z"/></svg>+44 (0)7700 900 418</p>
    <p class="contact contact--email"><svg viewBox="0 0 10 10"><path d="M0 2h10v6H0zm1 1 4 3 4-3z"/></svg>callum@haldenresolve.co.uk</p>

    <div class="rail" style="left:35px;top:220px;height:466px"></div>
    <h2 class="section-title" style="left:53px;top:247px">Training and Courses</h2>
    <div class="entries" style="left:57px;top:266px">
      <div class="timeline-row"><span>October 2021</span><span>The Guild of Property and Cost Surveyors, PCA Assessor Training</span></div>
      <div class="timeline-row"><span>October 2021</span><span>The College of Arbitral Practitioners<br>Diploma in International Arbitration (Module 1)</span></div>
      <div class="timeline-row"><span>December 2019</span><span>The Guild of Property and Cost Surveyors; PCA Counsellor Training</span></div>
      <div class="timeline-row timeline-row--gap"><span>2017 to 2019</span><span>The College of Arbitral Practitioners<br>Construction Adjudication Pathway<br>Module 1 – Law of Obligations and Civil Evidence<br>Module 2 – Construction Adjudication<br>Module 3 – Construction Adjudication<br>Module 4 – Decision Writing</span></div>
      <div class="timeline-row timeline-row--gap"><span>2017 to 2019</span><span>Kelvin University<br>Masters of Law, Construction Law (with Merit)<br>Legal Research<br>Law of the Construction Industry<br>Law and Practice of Construction Management<br>Legal Process and the Law of Contracts and Other Obligations<br>Dispute Resolution<br>Arbitration Law</span></div>
    </div>
    <h2 class="section-title" style="left:48px;top:549px">Employment History</h2>
    <div class="entries" style="left:57px;top:570px">
      <div class="history-row"><span>December 2018 to current</span><span>Director of Halden Resolve Ltd</span></div>
      <div class="history-row"><span>January 2017 to November 2018</span><span>Wardlaw and Pike Ltd (Contract &amp; Dispute Consultant)</span></div>
      <div class="history-row"><span>November 2015 to December 2016</span><span>Kelso Building Projects Ltd (Senior Quantity Surveyor)</span></div>
      <div class="history-row"><span>May 2015 to November 2015</span><span>Ashdown Retirement Lifestyles Ltd</span></div>
      <div class="history-row"><span>February 2014 to May 2015</span><span>DRM (Glasgow) Ltd – Contract Surveyor</span></div>
      <div class="history-row"><span>February 2013 to February 2014</span><span>Lennox &amp; Baird Ltd – Quantity Surveyor</span></div>
      <div class="history-row"><span>March 2012 to February 2013</span><span>Birchfield (Glasgow) Ltd – Quantity Surveyor</span></div>
      <div class="history-row"><span>July 2006 to March 2012</span><span>Corrie Group (Hargreave &amp; Brown) – Cost Consultant</span></div>
    </div>
    <div class="band-foot"></div>
  </article>

  <article class="page page--four">
    <div class="band-top"></div>
    <div class="brand">Halden Resolve</div>
    <div class="name-frame"></div>
    <div class="portrait" role="img" aria-label="Portrait photograph of Callum J Rennie on a blue circle"></div>
    <h1 class="name">Callum J Rennie</h1>
    <p class="creds">BSc (Hons), Dip.Adj, LL.M, FCAP, FGPCS, MSCWS, MSCM</p>
    <p class="contact contact--address"><svg viewBox="0 0 10 10"><path d="M5 0a3.5 3.5 0 0 0-3.5 3.5C1.5 6 5 10 5 10s3.5-4 3.5-6.5A3.5 3.5 0 0 0 5 0zm0 5a1.5 1.5 0 1 1 0-3 1.5 1.5 0 0 1 0 3z"/></svg>3rd Floor, 18 Corran Terrace, Glasgow, Scotland, United Kingdom, G3 7QL</p>
    <p class="contact contact--phone"><svg viewBox="0 0 10 10"><path d="M1 3c0-1 1-2 4-2s4 1 4 2l-2 1-.5-1h-3L3 4 1 3zm1.5 1.5h5L9 9H1z"/></svg>+44 (0)7700 900 418</p>
    <p class="contact contact--email"><svg viewBox="0 0 10 10"><path d="M0 2h10v6H0zm1 1 4 3 4-3z"/></svg>callum@haldenresolve.co.uk</p>

    <div class="rail" style="left:33px;top:216px;height:463px"></div>
    <div class="entries" style="left:59px;top:227px">
      <dl class="entry"><dt>Project:</dt><dd>Norvane Infrastructure, Data Centre Project, Sweden</dd><dt>Value:</dt><dd>Undisclosed</dd><dt>For:</dt><dd>Consulting for Veltrix International</dd><dt>Date:</dt><dd>January to February 2019</dd><dt>Services:</dt><dd>Review of Memorandum of Understanding, Norvane standard services contract, alignment<br>of contracts.</dd></dl>
      <dl class="entry"><dt>Project:</dt><dd>The Lancet Tower, London</dd><dt>For:</dt><dd>Facadia</dd><dt>Date:</dt><dd>2018</dd><dt>Services:</dt><dd>Contract and commercial management of BFC D&amp;B contract; dispute avoidance; claim<br>preparation for loss and/ or expense; legal opinion instructed from leading QC of 12<br>Ormond Chambers regarding liquidated damages clause within contract.</dd></dl>
      <dl class="entry entry--tight"><dt>Project:</dt><dd>Fuelcycle Energy, Kidderminster</dd><dt>Value:</dt><dd>c£5m</dd><dt>For:</dt><dd>Rainham Cladding Ltd</dd><dt>Date:</dt><dd>2017</dd><dt>Services:</dt><dd>Commercial management prior to adjudication, preparation of loss and/ or expense claim;<br>assisted with drafting the Referral and subsequent adjudication documents; attended<br><span class="outdent">hearing and assisted with representation of the Client.</span></dd></dl>
      <dl class="entry"><dt>Project:</dt><dd>Metro Rail Authority, LIFTWAY Schemes</dd><dt>Value:</dt><dd>c£5m</dd><dt>For:</dt><dd>Darrow Engineering Services Ltd</dd><dt>Date:</dt><dd>2018</dd><dt>Services:</dt><dd>Commercial and contract management of ECF3 contract.</dd></dl>
      <dl class="entry"><dt>Project:</dt><dd>Hamish Lyle Motors, Car Garage, Glasgow</dd><dt>Value:</dt><dd>c£6m</dd><dt>For:</dt><dd>Kelso Building Projects Ltd</dd><dt>Date:</dt><dd>2016</dd><dt>Services:</dt><dd>Commercial and contract management; preparation of claim for damages due to wrongful termina<br>tion of building contract, assisted Ferris Calder LLP with the quantum calculations and support<br>during the adjudication and assisted with the drafting and reviewing of adjudication submissions.</dd></dl>
    </div>
    <div class="band-foot"></div>
  </article>

</main>
</body>
</html>
```